Graphic Banner Design - 2.5' x 6' - High Tech Company

We are in need of a banner design for an outdoor sign that will be used at sponsorship events.

Size
2.5' x 6'

The company is a high tech company, and the design will be used for action sports events. So lining up to that would be good.

Tag line to be incorporated...
"Extreme IT Services for Extreme Needs."

Target Market(s)

Business Owners, Entrepreneurs, IT Professionals.

Industry/Entity Type

Information Technology

Logo Text

Vexlora

Colors

Designer to choose colors to be used in the design.

Requirements
Must have
• Must feel young and vibrant, fit in to an action sports event and just be out of this world awesome.
• In the world of the IT, we are the Zanverolli. Fast, Awesome, not necessarily cheap, but you know it will do what you want extremely well. Not for everyone, but always desired.

```html
<!DOCTYPE html>
<html lang="en">
<head>
<meta charset="utf-8">
<title>Vexlora Event Banner</title>
<link rel="stylesheet" href="https://fonts.googleapis.com/css2?family=Arimo:wght@400&family=Jost:wght@600&display=swap">
<style>
  :root {
    --backdrop: #c9c8c5;
    --banner-deep: #2e0b1f;
    --banner-mid: #5a2331;
    --glow-amber: #e8a04a;
    --glow-gold: #f6c878;
    --ink-light: #ffffff;
  }
  html, body {
    margin: 0;
    padding: 0;
    width: 1200px;
    height: 1200px;
    overflow: hidden;
    background: var(--backdrop);
  }
  .canvas {
    position: relative;
    width: 1200px;
    height: 1200px;
  }
  .banner {
    position: absolute;
    left: 66px;
    top: 338px;
    width: 1069px;
    height: 445px;
    overflow: hidden;
  }
  .banner-photo {
    position: absolute;
    inset: 0;
    background:
      radial-gradient(ellipse 140px 120px at 36% 52%, rgba(246,200,120,0.75), transparent 70%),
      radial-gradient(ellipse 150px 130px at 70% 50%, rgba(246,200,120,0.7), transparent 70%),
      radial-gradient(ellipse 130px 120px at 86% 56%, rgba(232,160,74,0.6), transparent 70%),
      radial-gradient(ellipse 420px 200px at 60% 20%, rgba(232,160,74,0.55), transparent 75%),
      radial-gradient(ellipse 300px 180px at 15% 25%, rgba(200,120,80,0.45), transparent 75%),
      linear-gradient(180deg, var(--banner-mid) 0%, #4a1a2c 45%, var(--banner-deep) 100%);
  }
  .brand-dot {
    position: absolute;
    left: 50%;
    top: 82px;
    width: 26px;
    height: 26px;
    margin-left: -13px;
    border-radius: 50%;
    background: var(--ink-light);
  }
  .brand-name {
    position: absolute;
    left: 0;
    right: 0;
    top: 178px;
    margin: 0;
    text-align: center;
    font-family: "Arimo", Arial, sans-serif;
    font-weight: 400;
    font-size: 94px;
    line-height: 1;
    color: var(--ink-light);
  }
  .tagline {
    position: absolute;
    left: 0;
    right: 0;
    top: 343px;
    margin: 0;
    text-align: center;
    font-family: "Jost", "Futura", sans-serif;
    font-weight: 600;
    font-size: 41px;
    line-height: 1;
    color: var(--ink-light);
  }
</style>
</head>
<body>
  <main class="canvas">
    <section class="banner">
      <div class="banner-photo" role="img" aria-label="Concert crowd with raised hands silhouetted against warm amber stage lights and falling sparks"></div>
      <span class="brand-dot"></span>
      <h1 class="brand-name">Vexlora</h1>
      <p class="tagline">Extreme IT Services for Extreme Needs.</p>
    </section>
  </main>
</body>
</html>
```